morvel family medicine business cards

create business cards for 7 family medicine providers and 4 admin using attached logo
2 locations
appointment reminder on back of cards
will provide more info regarding names,addresses, credentials etc once started

```html
<!DOCTYPE html>
<html lang="en">
<head>
<meta charset="utf-8">
<title>Morvel Family Medicine – Business Cards</title>
<link href="https://fonts.googleapis.com/css2?family=Cinzel:wght@500;600&family=Open+Sans:wght@400&display=swap" rel="stylesheet">
<style>
  :root {
    --navy: #2b2a6b;
    --sky: #2aa3dc;
    --paper: #ffffff;
    --backdrop: #d3d4d6;
  }
  * { margin: 0; padding: 0; box-sizing: border-box; }
  html, body { width: 900px; height: 1200px; overflow: hidden; background: var(--backdrop); }
  .canvas { position: relative; width: 900px; height: 1200px; }
  .card {
    position: absolute; left: 135px; width: 630px; height: 357px;
    background: var(--paper); border-radius: 14px;
  }
  .card--front { top: 215px; }
  .card--back { top: 628px; height: 360px; }
  .serif { font-family: "Cinzel", "Times New Roman", serif; font-weight: 600; }
  .sans { font-family: "Open Sans", Arial, sans-serif; }

  /* front */
  .brand { position: absolute; left: 40px; top: 70px; width: 240px; text-align: center; }
  .brand__mark { display: block; margin: 0 auto 14px; width: 96px; height: 96px; border-radius: 50%; background: linear-gradient(135deg, #4bb8e8, #1f8fcf); }
  .brand__name { color: var(--navy); font-size: 30px; line-height: 1.15; letter-spacing: 1px; }
  .reminder { position: absolute; left: 313px; top: 78px; color: var(--navy); font-size: 17px; line-height: 25px; letter-spacing: .6px; }
  .field { position: absolute; left: 313px; width: 283px; display: flex; align-items: flex-end; color: var(--sky); font-size: 17px; letter-spacing: .6px; }
  .field__line { flex: 1; margin-left: 6px; border-bottom: 1px solid var(--navy); height: 1px; margin-bottom: 5px; }
  .field--name { top: 166px; } .field--date { top: 208px; } .field--time { top: 250px; }
  .notice { position: absolute; left: 35px; top: 300px; color: var(--navy); font-size: 14.4px; letter-spacing: .2px; }

  /* back */
  .staff { position: absolute; left: 29px; top: 50px; list-style: none; color: var(--navy); }
  .staff li { font-size: 18px; height: 35.6px; letter-spacing: .3px; white-space: nowrap; }
  .staff .cred { color: var(--sky); font-weight: 500; }
  .staff .lead { font-size: 21px; height: 28px; }
  .staff .title { color: var(--sky); font-size: 13.5px; height: 33px; }
  .location { position: absolute; right: 27px; list-style: none; text-align: right; color: var(--navy); font-size: 15px; }
  .location li { height: 25.3px; display: flex; justify-content: flex-end; align-items: center; gap: 7px; }
  .location--one { top: 46px; } .location--two { top: 189px; }
  .icon { width: 14px; height: 14px; stroke: var(--sky); fill: none; stroke-width: 1.3; }
</style>
</head>
<body>
<div class="canvas">

  <section class="card card--front">
    <div class="brand">
      <span class="brand__mark" role="img" aria-label="Practice emblem"></span>
      <div class="brand__name serif">Morvel<br>Family Medicine</div>
    </div>
    <p class="reminder serif">Your next appointment is<br>scheduled for:</p>
    <div class="field field--name serif">Name:<span class="field__line"></span></div>
    <div class="field field--date serif">Date:<span class="field__line"></span></div>
    <div class="field field--time serif">Time:<span class="field__line"></span></div>
    <p class="notice sans">Please give 24 hours notice forcancellations to avoid a $50.00 no show fee.</p>
  </section>

  <section class="card card--back">
    <ul class="staff serif">
      <li class="lead">Dr. Owen Morvel, <span class="cred">D.O., P.A.</span></li>
      <li class="title">Board Certified Family Medicine</li>
      <li>Dr. Lena Morvel, <span class="cred">DNP</span></li>
      <li>Dr. Ruth Hallam, <span class="cred">DNP</span></li>
      <li>Nadia Ferrow, <span class="cred">APRN</span></li>
      <li>Dr. Celia Brantwood, <span class="cred">DNP</span></li>
      <li>Joanna Westlake, MSN, <span class="cred">APRN-BC</span></li>
      <li>Dr. Priya Ostrand, <span class="cred">MDSS</span></li>
    </ul>

    <ul class="location location--one sans">
      <li>4120 Alder Rd. #220</li>
      <li>Fernvale, FL 33012</li>
      <li>555-301-4410 <svg class="icon" viewBox="0 0 14 14"><path d="M3 1l2 3-1 1.5c.8 1.8 2.2 3.2 4 4L9.5 8.5l3 2-1 2C6 12 2 8 1.5 2.5z"/></svg></li>
      <li>555-301-4425 <svg class="icon" viewBox="0 0 14 14"><rect x="1" y="6" width="12" height="6"/><path d="M4 6V1.5h5l1 1V6"/></svg></li>
      <li>office@doctormorvel.com <svg class="icon" viewBox="0 0 14 14"><rect x="1" y="3" width="12" height="8"/><path d="M1 3l6 4.5L13 3"/></svg></li>
    </ul>
    <ul class="location location--two sans">
      <li>1850 N. Harbor Pkwy #201</li>
      <li>Lakeridge, FL 33029</li>
      <li>555-302-7730 <svg class="icon" viewBox="0 0 14 14"><path d="M3 1l2 3-1 1.5c.8 1.8 2.2 3.2 4 4L9.5 8.5l3 2-1 2C6 12 2 8 1.5 2.5z"/></svg></li>
      <li>555-302-7745 <svg class="icon" viewBox="0 0 14 14"><rect x="1" y="6" width="12" height="6"/><path d="M4 6V1.5h5l1 1V6"/></svg></li>
      <li>www.DoctorMorvel.com <svg class="icon" viewBox="0 0 14 14"><circle cx="7" cy="7" r="6"/><ellipse cx="7" cy="7" rx="2.6" ry="6"/><path d="M1 7h12M2 4h10M2 10h10"/></svg></li>
    </ul>
  </section>

</div>
</body>
</html>
```